Medical consulting firm needs polished website

I am a physician and working on setting up a smal consulting firm in New Hampshire, USA. It is called Clearpath Health Advisors, LLC and the website will be ClearpathHealthAdv.com. I was puttering around at making my own website, and it just didn't come together nicely so I've decided to leave it to the pros. The focus of the business is Advanced Care Planning, ie planning for your future medical needs. So it deals with some heavy stuff like planning for if you get sick, who should make decisions for you, end of life options etc. So it can't be too flippant or cutesy, but also can't be too dour and dark. I am hoping to convey that by thinking ahead and making some plans you can lift some of the worries off of yourself and your family - and that we can help make a scary sounding path more manageable. I want it to be made with wordpress and I have actually already bought a template ( Curova – A Bright Comprehensive Clinical & Wellness Theme ). The website needs to have general information about our services, doc profile, appointment maker, blog/url link page, and ideally web commerce application ( the template has access to woocommerce). I've posted my business card and current brochure (still tweaking them, but you get the idea). I am also partnering with lifeledgerhub.com and so have included their logo and would want connections/info about them. I have the logos etc in different formats as needed.

Target Market(s)

middle aged to older adults

Industry/Entity Type

Medical

Coding

Coded - Design and coding required

Font styles to use
Sans Serif

Requirements
Must have
• as above.
Nice to have
• Ease of reading/access for elderly viewers. woo commerce.

```html
<!DOCTYPE html>
<html lang="en">
<head>
<meta charset="utf-8">
<title>Clearpath Health Advisors, LLC</title>
<link href="https://fonts.googleapis.com/css2?family=Roboto+Condensed:wght@400;700&family=Architects+Daughter&display=swap" rel="stylesheet">
<style>
  :root {
    --white: #ffffff;
    --nav-blue: #4c9fe6;
    --band-blue: #5aa9ee;
    --button-blue: #1f6fc4;
    --hero-green: #57d21c;
    --hero-green-light: #8fdc86;
    --cta-green: #2fb52c;
    --ink: #222222;
    --muted: #6b6b6b;
    --photo-warm: #e9d8c4;
    --photo-soft: #cfe9b8;
  }
  * { box-sizing: border-box; margin: 0; padding: 0; }
  html, body { width: 1200px; height: 676px; overflow: hidden; background: var(--white); }
  body { font-family: "Roboto Condensed", Arial, sans-serif; color: var(--ink); position: relative; }

  .top-bar {
    height: 42px; display: flex; justify-content: flex-end; align-items: center;
    gap: 26px; padding-right: 40px; font-size: 13px; color: var(--muted);
  }
  .top-bar .contact-item { display: flex; align-items: center; gap: 5px; }
  .top-bar svg { width: 13px; height: 13px; fill: var(--muted); }
  .appointment-button {
    background: var(--cta-green); color: var(--white); font-weight: 700; font-size: 13px;
    padding: 3px 8px; border-radius: 3px;
  }
  .search-icon { width: 15px; height: 15px; }

  .main-nav {
    position: absolute; top: 42px; left: 0; width: 1200px; height: 70px;
    background: var(--nav-blue); display: flex; justify-content: flex-end; align-items: center;
    padding-right: 40px; gap: 36px;
  }
  .main-nav a {
    color: var(--white); text-decoration: none; font-size: 16px; text-transform: uppercase; font-weight: 400;
  }

  .brand {
    position: absolute; top: 30px; left: 50px; width: 290px; height: 96px; z-index: 2;
    background: var(--white); border-radius: 6px; box-shadow: 0 2px 6px rgba(0,0,0,.15);
    display: flex; align-items: center; gap: 12px; padding: 0 16px;
  }
  .brand-dot { width: 56px; height: 56px; border-radius: 50%; background: var(--nav-blue); flex: none; }
  .brand-name { color: var(--button-blue); font-size: 24px; line-height: 1.05; font-weight: 400; }

  .hero {
    position: absolute; top: 112px; left: 0; width: 1200px; height: 448px; overflow: hidden;
    background: linear-gradient(118deg, var(--hero-green) 0%, var(--hero-green) 48%, #6fd75a 48.2%, var(--hero-green-light) 100%);
  }
  .hero-photo {
    position: absolute; left: 280px; top: 90px; width: 320px; height: 358px;
    background: linear-gradient(180deg, var(--photo-soft) 0%, var(--photo-warm) 100%);
    border-radius: 150px 150px 0 0; opacity: .85;
  }
  .hero-copy { position: absolute; left: 720px; top: 150px; width: 420px; text-align: center; color: var(--white); }
  .hero-title { font-family: "Architects Daughter", cursive; font-size: 54px; font-weight: 400; line-height: 1; }
  .hero-text { margin-top: 20px; font-size: 15px; line-height: 1.3; }
  .register-button {
    display: inline-block; margin-top: 22px; background: var(--button-blue); color: var(--white);
    font-size: 10px; font-weight: 700; padding: 9px 14px; border-radius: 2px; letter-spacing: .3px;
  }
  .slider-dots { position: absolute; left: 590px; top: 422px; display: flex; gap: 8px; }
  .slider-dots span { width: 9px; height: 9px; border-radius: 50%; background: var(--white); }
  .slider-dots span.is-active { background: transparent; border: 1.5px solid var(--white); }

  .intro-band {
    position: absolute; top: 560px; left: 0; width: 1200px; height: 104px;
    background: var(--band-blue); color: var(--white); text-align: center; padding: 10px 60px 0;
  }
  .intro-band h1 { font-size: 22px; font-weight: 700; }
  .intro-rule { border: 0; border-top: 1.5px dashed rgba(255,255,255,.8); margin: 12px 0 12px; }
  .intro-band p { font-size: 13.5px; line-height: 1.35; }

  .services-heading {
    position: absolute; top: 664px; left: 0; width: 1200px; text-align: center;
    font-size: 22px; font-weight: 700; color: var(--ink);
  }
  .services-heading span { color: var(--button-blue); }
</style>
</head>
<body>
  <header>
    <div class="top-bar">
      <span class="contact-item">
        <svg viewBox="0 0 24 24"><path d="M6.6 10.8a15 15 0 0 0 6.6 6.6l2.2-2.2c.3-.3.7-.4 1-.2 1.1.4 2.3.6 3.6.6.6 0 1 .4 1 1V20c0 .6-.4 1-1 1A17 17 0 0 1 3 4c0-.6.4-1 1-1h3.5c.6 0 1 .4 1 1 0 1.3.2 2.5.6 3.6.1.3 0 .7-.2 1z"/></svg>
        +1 603 555 01 42
      </span>
      <span class="contact-item">
        <svg viewBox="0 0 24 24"><path d="M2 5h20v14H2z M2 5l10 8 10-8" fill="none" stroke="#6b6b6b" stroke-width="2"/></svg>
        info@clearpathhealthadv.com
      </span>
      <span class="appointment-button">Make an appointment</span>
      <svg class="search-icon" viewBox="0 0 24 24"><circle cx="10" cy="10" r="6.5" fill="none" stroke="#444" stroke-width="2.5"/><path d="M15 15l6 6" stroke="#444" stroke-width="2.5"/></svg>
    </div>

    <div class="brand">
      <span class="brand-dot"></span>
      <span class="brand-name">Clearpath<br>Health Advisors</span>
    </div>

    <nav class="main-nav">
      <a href="#">Home</a>
      <a href="#">About Us</a>
      <a href="#">Our Services</a>
      <a href="#">Team</a>
      <a href="#">Blog</a>
      <a href="#">Shop</a>
      <a href="#">Contact Us</a>
    </nav>
  </header>

  <section class="hero">
    <div class="hero-photo" role="img" aria-label="Photo of a smiling older couple embracing"></div>
    <div class="hero-copy">
      <h2 class="hero-title">Ready to Enjoy?</h2>
      <p class="hero-text">We are avaible to meet with you in the privacy of<br>your own home or in our office and provide notary serivces</p>
      <span class="register-button">REGISTER NOW</span>
    </div>
    <div class="slider-dots"><span class="is-active"></span><span></span><span></span><span></span></div>
  </section>

  <section class="intro-band">
    <h1>Clearpath Health Advisors, LLC</h1>
    <hr class="intro-rule">
    <p>Advanced Care Planning helps your voice to always be heard. None of us like to think about getting sick, injured, or even dying but.. unfortunately wishful thinking doesn't protect us, but<br>making a plane can help. We are here to help you arieve the peace of mind that comes from taking charge!</p>
  </section>

  <h2 class="services-heading">Our <span>Services</span></h2>
</body>
</html>
```